We operate a niche online Job Board in Australia. The website is called 'Harvest Roles Australia' and is used by Christian Employers to advertise their job vacancies.
I would like a business card that identifies with our website (www.harvestroles-example.com.au). We would like the same colors and fonts used on our business card from our website. When people look at our business card we want them to be able to recognise it from the website.
We want the web address to be dominant.
Updates
We are liking those that use white space as well as the blue and orange and those that highlight the url.
We now have 60 designs and therefore will not wait for the Sunday deadline to make a decision. We have a few we like.
The ones we like are:
- bold
- creative
- colorful (blue orange and white)
- some white space
- no boxes or borders
- font the same as our website
- reflects the look of our website
We will make a final decision in the next 6 hours so please if you think you have something to offer then get it in within the next 6 hours. If you think you will leave it till later you will miss out. Thanks to all those who have responded with some great designs, sorry we can't reward all of you!
Industry/Entity Type
Business
Contact Information for Business Card
Harvest Roles Australia
www.harvestroles-example.com.au
Peter Galvridge
CEO
Phone: 1300 512 874
Mobile: 0412 735019
Fax: (03) 9157 2360
email: peter@harvestroles-example.com.au
Requirements
Should not have
- We do not want a cross or any cliche christian images.

```html
<!DOCTYPE html>
<html lang="en">
<head>
<meta charset="utf-8">
<title>Harvest Roles Australia – Business Card</title>
<link rel="stylesheet" href="https://fonts.googleapis.com/css2?family=Arimo:wght@400;700&family=Noto+Serif:wght@400&family=Tinos&display=swap">
<style>
  :root {
    --navy: #0c1164;
    --orange: #f28c1e;
    --white: #ffffff;
    --ink: #111111;
    --backdrop: #2b2b2b;
  }
  * { box-sizing: border-box; margin: 0; padding: 0; }
  html, body { width: 1200px; height: 942px; overflow: hidden; }
  body {
    background: var(--backdrop);
    font-family: "Arimo", Arial, sans-serif;
    position: relative;
  }
  .card {
    position: absolute;
    top: 321px;
    width: 520px;
    height: 300px;
    overflow: hidden;
  }

  /* Front */
  .card--front { left: 60px; background: var(--navy); }
  .front-name {
    position: absolute;
    left: 70px; top: 92px;
    font-family: "Noto Serif", Georgia, serif;
    font-size: 50px;
    color: var(--white);
    letter-spacing: -0.5px;
  }
  .front-band {
    position: absolute;
    left: 0; right: 0; bottom: 28px;
    height: 44px;
    background: var(--orange);
    display: flex; align-items: center; justify-content: flex-end;
    padding-right: 28px;
  }
  .front-url {
    color: var(--white);
    font-weight: 700;
    font-size: 19px;
    letter-spacing: 1.5px;
  }

  /* Back */
  .card--back { left: 620px; background: var(--white); }
  .back-band {
    position: absolute;
    left: 22px; right: 22px; top: 22px;
    height: 40px;
    background: var(--navy);
    display: flex; align-items: center; justify-content: space-between;
    padding: 0 8px 0 10px;
  }
  .back-brand {
    font-family: "Noto Serif", Georgia, serif;
    font-size: 16px;
    color: var(--white);
  }
  .back-url {
    background: var(--white);
    color: var(--ink);
    font-size: 14px;
    padding: 3px 7px;
  }
  .person {
    position: absolute;
    left: 60px; top: 100px;
    font-weight: 700;
    font-size: 29px;
    color: var(--ink);
  }
  .contacts {
    position: absolute;
    left: 110px; top: 150px;
    list-style: none;
  }
  .contacts li {
    display: flex; align-items: center; gap: 10px;
    height: 30px;
  }
  .contacts .email { font-size: 15px; color: var(--ink); }
  .contacts .mobile { font-family: "Tinos", "Times New Roman", serif; font-size: 18px; color: var(--ink); }
  .icon { width: 22px; height: 18px; flex: none; }
  .back-footer {
    position: absolute;
    left: 0; right: 0; bottom: 0;
    height: 40px;
    background: var(--orange);
    display: flex; align-items: center; justify-content: space-between;
    padding: 0 24px;
    font-family: "Tinos", "Times New Roman", serif;
    font-size: 17px;
    color: var(--ink);
  }
  .back-footer .label {
    font-family: "Arimo", Arial, sans-serif;
    font-weight: 700;
    font-size: 15px;
    color: var(--navy);
  }
</style>
</head>
<body>
  <section class="card card--front" aria-label="Card front">
    <p class="front-name">Harvest Roles</p>
    <div class="front-band"><span class="front-url">www.harvestroles-example.com.au</span></div>
  </section>

  <section class="card card--back" aria-label="Card back">
    <div class="back-band">
      <span class="back-brand">Harvest Roles Australia</span>
      <span class="back-url">www.harvestroles-example.com.au</span>
    </div>
    <p class="person">Peter Galvridge CEO</p>
    <ul class="contacts">
      <li>
        <svg class="icon" viewBox="0 0 22 18" aria-hidden="true">
          <rect x="1" y="2" width="20" height="14" fill="#fff" stroke="#0c1164" stroke-width="1.5"/>
          <path d="M1 2 L11 10 L21 2" fill="none" stroke="#0c1164" stroke-width="1.5"/>
        </svg>
        <span class="email">peter@harvestroles-example.com.au</span>
      </li>
      <li>
        <svg class="icon" viewBox="0 0 22 18" aria-hidden="true">
          <rect x="6" y="0.5" width="10" height="17" rx="1.5" fill="#fff" stroke="#0c1164" stroke-width="1.5"/>
          <rect x="8" y="3" width="6" height="6" fill="#0c1164"/>
        </svg>
        <span class="mobile">0412 735019</span>
      </li>
    </ul>
    <div class="back-footer">
      <span><span class="label">Phone:</span> 1300 512 874</span>
      <span><span class="label">Fax:</span> (03) 9157 2360</span>
    </div>
  </section>
</body>
</html>
```